Need help in designing new business card utilizing our new logo.

BuildMarq Solutions works with Construction Business Owners, Managers & IT Professionals to strengthen software usage and increase user productivity.

Our Construction Accounting and Mobile Field Management Software Clients engage with us in the following areas:

New Software Implementations
Software Re-Implementations
Redesigning Software Usage at the User Level
Project Coordination & Management
Continued Software Support

Old tag line:
Clear Choices - Practical Results

www.buildmarq-solutions.example

Stride 4 is a product, but not needed for a new business card.

```html
<!DOCTYPE html>
<html lang="en">
<head>
<meta charset="utf-8">
<title>BuildMarq Solutions – Business Card</title>
<link rel="stylesheet" href="https://fonts.googleapis.com/css2?family=Raleway:wght@400;500;600&display=swap">
<style>
  :root {
    --backdrop: #1DA9EC;
    --card: #ffffff;
    --navy: #2B3990;
    --grey: #C8C9CB;
    --grey-text: #9A9DA2;
    --body-text: #4A4D55;
  }
  * { margin: 0; padding: 0; box-sizing: border-box; }
  html, body { width: 1200px; height: 1145px; overflow: hidden; }
  body {
    background: var(--backdrop);
    font-family: "Raleway", sans-serif;
    position: relative;
  }
  .card {
    position: absolute;
    left: 237px;
    width: 674px;
    background: var(--card);
    overflow: hidden;
  }
  .card--front { top: 132px; height: 399px; }
  .card--back  { top: 622px; height: 396px; }
  .card__shapes { position: absolute; inset: 0; width: 100%; height: 100%; }

  /* Front */
  .brand {
    position: absolute; left: 253px; top: 52px;
    display: flex; align-items: center; gap: 12px;
  }
  .brand__mark { width: 36px; height: 36px; background: var(--navy); flex: none; }
  .brand__name {
    color: var(--navy); font-weight: 600; font-size: 22px;
    letter-spacing: 0.5px; text-transform: uppercase; white-space: nowrap;
  }
  .tagline {
    position: absolute; left: 253px; width: 360px; top: 144px;
    text-align: center; font-size: 14.5px; color: var(--grey-text); font-weight: 500;
    white-space: nowrap;
  }
  .person__name {
    position: absolute; left: 250px; top: 197px;
    font-size: 31px; color: var(--navy); font-weight: 500;
  }
  .person__role {
    position: absolute; left: 251px; top: 237px;
    font-size: 21px; color: var(--grey); font-weight: 500;
  }
  .contact { position: absolute; left: 254px; top: 286px; list-style: none; }
  .contact li {
    display: flex; align-items: center; gap: 8px;
    height: 29px; font-size: 14px; color: var(--body-text); white-space: nowrap;
  }
  .contact svg { width: 13px; height: 13px; fill: var(--navy); flex: none; }

  /* Back */
  .services__title {
    position: absolute; left: 107px; top: 58px;
    font-size: 31px; color: var(--navy); font-weight: 500;
  }
  .services__list {
    position: absolute; left: 82px; top: 107px; list-style: none;
    font-size: 20px; line-height: 44px; color: var(--body-text);
  }
  .services__list li { position: relative; padding-left: 28px; }
  .services__list li::before {
    content: ""; position: absolute; left: 0; top: 13px;
    width: 18px; height: 18px; border-radius: 50%; background: var(--grey);
  }
  .services__list li.is-accent::before { background: var(--navy); }
</style>
</head>
<body>

<section class="card card--front" aria-label="Business card front">
  <svg class="card__shapes" viewBox="0 0 245 145" preserveAspectRatio="none" aria-hidden="true">
    <polygon points="0,0 70,0 0,32" fill="var(--grey)"/>
    <polygon points="0,32 72,142 0,118" fill="var(--navy)"/>
    <polygon points="0,120 40,145 0,145" fill="var(--grey)"/>
  </svg>

  <div class="brand">
    <span class="brand__mark"></span>
    <span class="brand__name">BuildMarq Solutions</span>
  </div>
  <p class="tagline">Clear Choices - Practical Results</p>

  <h1 class="person__name">Dana R Whitlow</h1>
  <p class="person__role">Owner</p>

  <ul class="contact">
    <li>
      <svg viewBox="0 0 16 16"><path d="M8 1 1 7h2v8h4v-5h2v5h4V7h2z"/></svg>
      866-555-0142 ext 100
    </li>
    <li>
      <svg viewBox="0 0 16 16"><circle cx="8" cy="8" r="7"/></svg>
      dana.whitlow@buildmarq.example
    </li>
    <li>
      <svg viewBox="0 0 16 16"><path d="M4 1c1 0 2 3 2 4s-2 1-1 3 2 3 3 3 1-2 3-1 4 1 4 2-2 3-4 3C6 15 1 10 1 4c0-2 2-3 3-3z"/></svg>
      518-555-0163
    </li>
  </ul>
</section>

<section class="card card--back" aria-label="Business card back">
  <svg class="card__shapes" viewBox="0 0 245 144" preserveAspectRatio="none" aria-hidden="true">
    <polygon points="182,0 232,0 245,22 245,58" fill="var(--navy)"/>
    <polygon points="232,0 245,0 245,22" fill="var(--grey)"/>
    <polygon points="180,144 245,90 245,144" fill="var(--grey)"/>
  </svg>

  <h2 class="services__title">Services</h2>
  <ul class="services__list">
    <li>New Software Implementations</li>
    <li class="is-accent">Software Re-Implementations</li>
    <li>Project Coordination &amp; Management</li>
    <li class="is-accent">Continued Software Support</li>
    <li>Redesigning Software Usage at the<br>User Level</li>
  </ul>
</section>

</body>
</html>
```